Business Card for Web Design consulting firm

Business card designs for Web Design consulting firm

Target Market(s)

English speaking adults ages 30 - 60. Predominantly professional services eg. Doctor, Dentist

Industry/Entity Type

Consulting

Requirements
Must have
• Double sided card

```html
<!DOCTYPE html>
<html lang="en">
<head>
<meta charset="utf-8">
<title>Lumetra – Business Card</title>
<link href="https://fonts.googleapis.com/css2?family=Carlito:wght@400;700&display=swap" rel="stylesheet">
<style>
  :root {
    --page-bg: #ffffff;
    --card-bg: #f6f9f8;
    --card-edge: #e3e8e7;
    --ink-dark: #4a4f4f;
    --ink-mid: #5b6060;
    --accent-orange: #f7941d;
  }
  html, body {
    margin: 0;
    padding: 0;
    width: 1200px;
    height: 1046px;
    overflow: hidden;
    background: var(--page-bg);
    font-family: "Carlito", "Calibri", Arial, sans-serif;
  }
  .canvas {
    position: relative;
    width: 1200px;
    height: 1046px;
  }
  .card {
    position: absolute;
    background: var(--card-bg);
    border: 1px solid var(--card-edge);
    box-sizing: border-box;
    color: var(--ink-dark);
  }
  /* Front side */
  .card-front {
    left: 137px;
    top: 87px;
    width: 625px;
    height: 388px;
  }
  .front-brand {
    position: absolute;
    left: 0;
    right: 0;
    top: 150px;
    display: flex;
    align-items: center;
    justify-content: center;
    gap: 18px;
  }
  .brand-square {
    width: 34px;
    height: 34px;
    background: var(--accent-orange);
  }
  .brand-name {
    font-weight: 700;
    color: var(--ink-dark);
    letter-spacing: 0.12em;
    line-height: 1;
  }
  .front-brand .brand-name { font-size: 72px; }
  .tagline {
    position: absolute;
    left: 0;
    right: 0;
    top: 322px;
    text-align: center;
    font-size: 21px;
    color: var(--ink-dark);
  }
  /* Back side */
  .card-back {
    left: 387px;
    top: 517px;
    width: 638px;
    height: 363px;
  }
  .back-brand {
    position: absolute;
    left: 38px;
    top: 42px;
    display: flex;
    align-items: center;
    gap: 10px;
  }
  .back-brand .brand-square { width: 18px; height: 18px; }
  .back-brand .brand-name { font-size: 30px; }
  .person {
    position: absolute;
    right: 38px;
    top: 30px;
    text-align: right;
  }
  .person-name {
    margin: 0;
    font-size: 40px;
    font-weight: 700;
    color: var(--ink-dark);
    line-height: 1.1;
  }
  .person-title {
    margin: 2px 0 0;
    font-size: 19px;
    font-weight: 700;
    color: var(--ink-mid);
  }
  .details {
    position: absolute;
    top: 148px;
    margin: 0;
    padding: 0;
    list-style: none;
    font-size: 20px;
    font-weight: 700;
    line-height: 30px;
    color: var(--ink-mid);
  }
  .address { left: 38px; }
  .contact { right: 38px; text-align: right; }
  .web-address {
    position: absolute;
    left: 0;
    right: 0;
    bottom: 18px;
    text-align: center;
    font-size: 20px;
    font-weight: 700;
    color: var(--ink-mid);
  }
</style>
</head>
<body>
<main class="canvas">
  <section class="card card-front" aria-label="Card front">
    <div class="front-brand">
      <span class="brand-square"></span>
      <span class="brand-name">LUMETRA</span>
    </div>
    <p class="tagline">Web Design Consulting</p>
  </section>

  <section class="card card-back" aria-label="Card back">
    <div class="back-brand">
      <span class="brand-square"></span>
      <span class="brand-name">LUMETRA</span>
    </div>
    <div class="person">
      <h1 class="person-name">John Smith</h1>
      <p class="person-title">Job title</p>
    </div>
    <ul class="details address">
      <li>Address 1</li>
      <li>Address 2</li>
      <li>Address 3</li>
    </ul>
    <ul class="details contact">
      <li>E-mail</li>
      <li>Phone</li>
      <li>Cell</li>
      <li>Fax</li>
    </ul>
    <p class="web-address">Web Address</p>
  </section>
</main>
</body>
</html>
```